Products & Services Postcard For our Vacuum Repair Store & Carpet Cleaning Company

SEE ATTACHED DOCUMENTS FOR FRONT AND BACK OF CARD.
Also, Brand logos are available in my attachments

We are a Retail Vacuum Repair shop and we also have Three carpet cleaning trucks that operate out of our location. In addition to servicing Vacuum Cleaners we also offer in home cleaning services that include: Carpet cleaning, upholstery cleaning, tile & Grout Cleaning, general cleaning services, move out clean ups, one time cleanings, post construction cleanup and strip & wax floorsWe Need to design a KTRW(nbfl kestrel lane route) postcard that shows and tells everything we do. Postcard should include all our services, have before and after pictures, list benefits of doing business with us and should have coupons attached to create urgency to call usWe:Fully Insured, commercial & Residential, free estimatesWe are the only Vacuum Store in area that is a Certified OTWAB Cleaner.Also, the only OTWAB Certified cleaner that services Vacuum Cleaners.We have a great reputation as a 5 Star Vacuum Service Station and Also a 5 Star Cleaning Company. We are a one stop shop for ALL your cleaning needs.Our goal is to educate customers and provide options.Goal of the card is to get customers to call or stop in for advice on both their vacuum cleaner and cleaning their homes. Goal is to get phone to ring or get people through the door.

Target Market(s)

Homeowners, People interested in clean

Colors

Designer to choose colors to be used in the design.

Requirements
Must have
• Before & After pics
• Coupons
• List of services
• Call to Action
• Address
• Phone #
Nice to have
• One side of postcard could be about our Vacuum Cleaner repair shop.
• The other side could be about our cleaning business

```html
<!DOCTYPE html>
<html lang="en">
<head>
<meta charset="utf-8">
<title>Vacuum Repair &amp; Cleaning Postcard</title>
<link rel="stylesheet" href="https://fonts.googleapis.com/css2?family=Roboto+Condensed:wght@400;700&family=Open+Sans:wght@300;400;600;700&display=swap">
<style>
  :root {
    --stage: #262626;
    --white: #ffffff;
    --navy: #0f1f45;
    --teal-ink: #1c5c70;
    --blue-light: #0a8fb0;
    --blue-mid: #0f73a0;
    --blue-deep: #135386;
    --coupon-top: #1a6d95;
    --coupon-bottom: #0f4e72;
    --tile: rgba(255,255,255,0.12);
    --footer: #1b5f72;
    --photo-light: #e9ecee;
    --photo-mid: #c9d0d5;
    --badge: #1a1a1a;
  }
  * { box-sizing: border-box; margin: 0; padding: 0; }
  html, body { width: 1200px; height: 1000px; overflow: hidden; }
  body { background: var(--stage); position: relative; font-family: "Open Sans", Arial, sans-serif; }

  .card { position: absolute; overflow: hidden; background: var(--white); }
  .card--front { left: 179px; top: 103px; width: 671px; height: 372px; }
  .card--back { left: 371px; top: 508px; width: 670px; height: 372px; }
  .card svg.shapes { position: absolute; left: 0; top: 0; }

  .logo { position: absolute; color: var(--navy); }
  .logo__name { font-family: "Open Sans", Arial, sans-serif; font-weight: 700; font-size: 22px; line-height: 25px; letter-spacing: -0.3px; }
  .logo__tag { font-family: "Open Sans", Arial, sans-serif; font-weight: 300; font-size: 8.5px; letter-spacing: 0.2px; margin-top: 2px; }
  .card--front .logo { left: 22px; top: 20px; }

  .headline { position: absolute; left: 31px; top: 112px; font-family: "Roboto Condensed", Arial, sans-serif; font-weight: 700; font-size: 32px; line-height: 38px; color: var(--teal-ink); }

  .coupon { position: absolute; top: 249px; width: 111px; height: 116px; color: var(--white); background: linear-gradient(180deg, var(--coupon-top), var(--coupon-bottom)); padding: 0 6px; }
  .coupon--one { left: 24px; }
  .coupon--two { left: 154px; }
  .coupon--three { left: 284px; top: 239px; height: 126px; width: 133px; background: none; padding: 0 8px; }
  .coupon__price { font-family: "Roboto Condensed", Arial, sans-serif; font-weight: 700; font-size: 30px; text-align: right; margin-top: 8px; line-height: 34px; }
  .coupon__price sup { font-size: 17px; vertical-align: 9px; }
  .coupon__text { font-family: "Roboto Condensed", Arial, sans-serif; font-size: 7.6px; font-weight: 700; line-height: 9.6px; margin-top: 10px; }
  .coupon__off { position: relative; font-family: "Roboto Condensed", Arial, sans-serif; font-weight: 700; text-align: right; line-height: 28px; margin-top: 8px; padding-right: 12px; }
  .coupon__off b { font-size: 32px; display: block; }
  .coupon__off span { font-size: 19px; display: block; line-height: 18px; }
  .coupon__code { position: relative; font-family: "Roboto Condensed", Arial, sans-serif; font-weight: 700; font-size: 14px; margin-top: 4px; }
  .coupon--three .coupon__text { position: relative; margin-top: 2px; }

  .badge { position: absolute; left: 611px; top: 18px; width: 40px; height: 60px; }

  .rating { position: absolute; color: var(--white); text-align: center; font-size: 8.5px; }
  .rating svg { display: block; margin: 0 auto 6px; }
  .rating--vacuum { left: 470px; top: 64px; width: 123px; }
  .rating--cleaning { left: 500px; top: 141px; width: 123px; }

  .contact { position: absolute; color: var(--white); }
  .contact__label { font-family: "Roboto Condensed", Arial, sans-serif; font-weight: 700; font-size: 14px; }
  .contact--phone { left: 443px; top: 231px; }
  .phone { display: flex; align-items: center; gap: 8px; margin-top: 2px; font-family: "Open Sans", Arial, sans-serif; font-weight: 600; font-size: 25px; letter-spacing: 0.5px; }
  .phone__or { font-size: 6px; display: block; margin: -4px 0 0 107px; }
  .contact--visit { left: 432px; top: 293px; }
  .address { margin-top: 8px; font-size: 11.5px; line-height: 14px; text-align: right; width: 214px; }

  .services__title { position: absolute; left: 34px; top: 24px; color: var(--white); font-size: 24px; font-weight: 400; letter-spacing: 0.2px; }
  .tile { position: absolute; display: flex; align-items: center; justify-content: center; text-align: center; background: var(--tile); color: var(--white); font-size: 11.5px; line-height: 14px; font-weight: 400; }
  .tile--a { width: 111px; height: 62px; }
  .tile--b { width: 141px; height: 63px; }
  .back-footer { position: absolute; left: 0; top: 305px; width: 400px; height: 67px; background: var(--footer); }
  .back-footer .logo { left: 26px; top: 6px; color: var(--white); }
  .back-footer .logo__name { font-size: 14px; line-height: 17px; }
  .back-footer .logo__tag { font-size: 5px; margin-top: 1px; }
</style>
</head>
<body>

<section class="card card--front">
  <svg class="shapes" width="671" height="372" viewBox="0 0 671 372">
    <defs>
      <linearGradient id="photoTone" x1="0" y1="0" x2="1" y2="1">
        <stop offset="0" stop-color="var(--photo-light)"/>
        <stop offset="1" stop-color="var(--photo-mid)"/>
      </linearGradient>
      <linearGradient id="panelBlue" x1="0" y1="0" x2="1" y2="0">
        <stop offset="0" stop-color="var(--blue-deep)"/>
        <stop offset="1" stop-color="var(--blue-light)"/>
      </linearGradient>
      <linearGradient id="couponBlue" x1="0" y1="0" x2="0" y2="1">
        <stop offset="0" stop-color="var(--coupon-top)"/>
        <stop offset="1" stop-color="var(--coupon-bottom)"/>
      </linearGradient>
    </defs>
    <polygon role="img" aria-label="Photo of a carpet cleaning wand extracting dirt from a light carpet"
             points="211,0 420,0 466,187 420,372 211,372 266,82" fill="url(#photoTone)"/>
    <polygon points="409,0 671,0 671,372 409,372 466,187" fill="url(#panelBlue)"/>
    <polygon points="284,239 417,239 409,365 284,365" fill="url(#couponBlue)"/>
  </svg>

  <div class="logo">
    <div class="logo__name">YOUR<br>LOGO</div>
    <div class="logo__tag">RETAIL VACUUM REPAIR SHOP</div>
  </div>

  <h1 class="headline">One Stop Shop<br>For ALL Your<br>Cleaning Needs</h1>

  <div class="coupon coupon--one">
    <div class="coupon__price"><sup>$</sup>99</div>
    <p class="coupon__text">Lorem ipsum dolor sit amet, consectetuer adipiscing elit, sed diam nonummy nibh euismod tincidunt ut laoreet dolore magna aliquam erat</p>
  </div>
  <div class="coupon coupon--two">
    <div class="coupon__price"><sup>$</sup>99</div>
    <p class="coupon__text">Lorem ipsum dolor sit amet, consectetuer adipiscing elit, sed diam nonummy nibh euismod tincidunt ut laoreet dolore magna aliquam erat</p>
  </div>
  <div class="coupon coupon--three">
    <div class="coupon__off"><b>20%</b><span>OFF</span></div>
    <div class="coupon__code">Coupon Code:</div>
    <p class="coupon__text">Lorem ipsum dolor sit amet, consectetuer adipiscing elit, sed diam nonummy nibh</p>
  </div>

  <svg class="badge" viewBox="0 0 40 60" role="img" aria-label="OTWAB certification badge">
    <rect x="1" y="1" width="38" height="58" rx="19" fill="var(--badge)"/>
    <circle cx="20" cy="20" r="13" fill="var(--white)"/>
  </svg>

  <div class="rating rating--vacuum">
    <svg width="64" height="34" viewBox="0 0 64 34" aria-hidden="true">
      <g fill="var(--white)">
        <polygon transform="translate(20,8)" points="0,-8 2.3,-2.5 8,-2.5 3.4,1 5,7 0,3.6 -5,7 -3.4,1 -8,-2.5 -2.3,-2.5"/>
        <polygon transform="translate(40,8)" points="0,-8 2.3,-2.5 8,-2.5 3.4,1 5,7 0,3.6 -5,7 -3.4,1 -8,-2.5 -2.3,-2.5"/>
        <polygon transform="translate(10,25)" points="0,-8 2.3,-2.5 8,-2.5 3.4,1 5,7 0,3.6 -5,7 -3.4,1 -8,-2.5 -2.3,-2.5"/>
        <polygon transform="translate(30,25)" points="0,-8 2.3,-2.5 8,-2.5 3.4,1 5,7 0,3.6 -5,7 -3.4,1 -8,-2.5 -2.3,-2.5"/>
        <polygon transform="translate(50,25)" points="0,-8 2.3,-2.5 8,-2.5 3.4,1 5,7 0,3.6 -5,7 -3.4,1 -8,-2.5 -2.3,-2.5"/>
      </g>
    </svg>
    Vacuum Service Station
  </div>
  <div class="rating rating--cleaning">
    <svg width="64" height="34" viewBox="0 0 64 34" aria-hidden="true">
      <g fill="var(--white)">
        <polygon transform="translate(20,8)" points="0,-8 2.3,-2.5 8,-2.5 3.4,1 5,7 0,3.6 -5,7 -3.4,1 -8,-2.5 -2.3,-2.5"/>
        <polygon transform="translate(40,8)" points="0,-8 2.3,-2.5 8,-2.5 3.4,1 5,7 0,3.6 -5,7 -3.4,1 -8,-2.5 -2.3,-2.5"/>
        <polygon transform="translate(10,25)" points="0,-8 2.3,-2.5 8,-2.5 3.4,1 5,7 0,3.6 -5,7 -3.4,1 -8,-2.5 -2.3,-2.5"/>
        <polygon transform="translate(30,25)" points="0,-8 2.3,-2.5 8,-2.5 3.4,1 5,7 0,3.6 -5,7 -3.4,1 -8,-2.5 -2.3,-2.5"/>
        <polygon transform="translate(50,25)" points="0,-8 2.3,-2.5 8,-2.5 3.4,1 5,7 0,3.6 -5,7 -3.4,1 -8,-2.5 -2.3,-2.5"/>
      </g>
    </svg>
    Cleaning Company
  </div>

  <div class="contact contact--phone">
    <div class="contact__label">CONTACT:</div>
    <div class="phone">
      <svg width="24" height="24" viewBox="0 0 24 24" aria-hidden="true">
        <circle cx="12" cy="12" r="12" fill="var(--white)"/>
        <path d="M8.2 6.2c.5-.4 1.1-.3 1.4.2l1.2 2c.3.5.2 1-.2 1.4l-.7.6c.6 1.4 1.7 2.6 3.1 3.3l.7-.7c.4-.4 1-.4 1.4-.1l2 1.3c.5.3.6 1 .2 1.4l-1 1.1c-.6.6-1.5.8-2.3.5-3.1-1.1-5.4-3.5-6.5-6.6-.3-.8 0-1.7.6-2.3z" fill="var(--blue-mid)"/>
      </svg>
      <span>0147 258 369</span>
    </div>
    <span class="phone__or">or</span>
  </div>
  <div class="contact contact--visit">
    <div class="contact__label">VISIT US:</div>
    <p class="address">418 NW, 22nd Avenue Number, FL, 33190<br>Your Country Name</p>
  </div>
</section>

<section class="card card--back">
  <svg class="shapes" width="670" height="372" viewBox="0 0 670 372">
    <defs>
      <linearGradient id="backBlue" x1="0" y1="0" x2="1" y2="0">
        <stop offset="0" stop-color="var(--blue-light)"/>
        <stop offset="1" stop-color="var(--blue-deep)"/>
      </linearGradient>
    </defs>
    <polygon points="0,0 387,0 444,87 400,372 0,372" fill="url(#backBlue)"/>
  </svg>

  <h2 class="services__title">Services we offer</h2>

  <div class="tile tile--a" style="left:31px;top:71px;">CARPET<br>CLEANING</div>
  <div class="tile tile--a" style="left:157px;top:71px;">UPHOLSTERY<br>CLEANING</div>
  <div class="tile tile--a" style="left:285px;top:71px;">TILE &amp; GROUT<br>CLEANING</div>
  <div class="tile tile--a" style="left:31px;top:151px;">MOVE OUT<br>CLEAN UPS</div>
  <div class="tile tile--a" style="left:157px;top:151px;">ONE TIME<br>CLEANINGS</div>
  <div class="tile tile--a" style="left:285px;top:151px;">STRIP &amp;<br>WAX FLOORS</div>
  <div class="tile tile--b" style="left:69px;top:229px;">GENERAL<br>CLEANING SERVICES</div>
  <div class="tile tile--b" style="left:229px;top:230px;">POST CONS-<br>TRUCTION CLEANUP</div>

  <div class="back-footer">
    <div class="logo">
      <div class="logo__name">YOUR<br>LOGO</div>
      <div class="logo__tag">RETAIL VACUUM REPAIR SHOP</div>
    </div>
  </div>
</section>

</body>
</html>
```